The Book Cover for "Finding the Silver Lantern of Dawn" needs redesigned

First the back ground or art work needs to be replaced or redesigned.
The title Finding the Silver Lantern of Dawn needs to be redesigned so that the words "Finding the" is diminished in size compared to the rest of the title "Silver Lantern of Dawn"
The Sub-title "Tracing the forgotten path of the Evening Wind" needs to be more pronounced and readable.
The authors name needs to be downsized.

```html
<!DOCTYPE html>
<html lang="en">
<head>
<meta charset="utf-8">
<title>Finding the Silver Lantern of Dawn — Book Cover</title>
<link rel="stylesheet" href="https://fonts.googleapis.com/css2?family=Tinos:wght@700&family=Open+Sans:wght@400;600;700&display=swap">
<style>
  :root {
    --paper: #ffffff;
    --ink: #0b0b0b;
    --subtitle-ink: #111111;
    --art-dark: #1a1612;
    --art-mid: #4a3826;
    --art-gold: #c08a42;
    --art-glow: #f6ead0;
  }
  html, body {
    margin: 0;
    padding: 0;
    overflow: hidden;
    background: var(--paper);
  }
  .cover {
    position: relative;
    width: 800px;
    height: 1200px;
    background: var(--paper);
    overflow: hidden;
    color: var(--ink);
  }
  .title {
    position: absolute;
    left: 0;
    right: 0;
    top: 56px;
    margin: 0;
    text-align: center;
    font-family: "Tinos", "Times New Roman", serif;
    font-weight: 700;
    line-height: 1;
  }
  .title-lead {
    display: block;
    font-size: 32px;
    letter-spacing: 1px;
  }
  .title-main {
    display: block;
    font-size: 64px;
    margin-top: 14px;
    letter-spacing: 0.5px;
  }
  .title-final {
    display: block;
    font-size: 230px;
    line-height: 0.86;
    margin-top: 18px;
    letter-spacing: 2px;
  }
  .subtitle {
    position: absolute;
    left: 40px;
    right: 40px;
    top: 424px;
    margin: 0;
    text-align: center;
    font-family: "Open Sans", Arial, sans-serif;
    font-weight: 600;
    font-size: 25px;
    line-height: 1.3;
    letter-spacing: 0.8px;
    color: var(--subtitle-ink);
  }
  .cover-art {
    position: absolute;
    left: 110px;
    top: 490px;
    width: 580px;
    height: 550px;
  }
  .author {
    position: absolute;
    left: 0;
    right: 0;
    top: 1102px;
    margin: 0;
    text-align: center;
    font-family: "Open Sans", Arial, sans-serif;
    font-weight: 700;
    font-size: 22px;
    letter-spacing: 3px;
  }
</style>
</head>
<body>
  <div class="cover">
    <h1 class="title">
      <span class="title-lead">FINDING THE</span>
      <span class="title-main">SILVER LANTERN OF</span>
      <span class="title-final">DAWN</span>
    </h1>
    <p class="subtitle">Tracing the forgotten path of the Evening Wind</p>

    <svg class="cover-art" viewBox="0 0 580 550" role="img"
         aria-label="Cover artwork: new central illustration in dark umber and warm gold tones with a radiant glowing centre">
      <defs>
        <radialGradient id="artGlow" cx="50%" cy="50%" r="60%">
          <stop offset="0%" stop-color="var(--art-glow)"/>
          <stop offset="16%" stop-color="var(--art-gold)"/>
          <stop offset="48%" stop-color="var(--art-mid)"/>
          <stop offset="100%" stop-color="var(--art-dark)"/>
        </radialGradient>
      </defs>
      <rect x="0" y="0" width="580" height="550" rx="18" fill="url(#artGlow)"/>
    </svg>

    <p class="author">J R ALDEN ALDERWOOD</p>
  </div>
</body>
</html>
```